Monument sign* - Law Firm

*I am installing a monument sign that has LED, as well as backlit elements. I am seeking help in designing the backlit portion of the sign. The Backlit sign will be 12’ x 4’.

We are looking for a classic, yet eye-catching sign to help new and current clients find our firm as well as bring in future clients. One of our goals is that people who drive by on a regular basis remember our sign (and us) for any future legal need.

Target Market(s)

Current and future clientele

Industry/Entity Type

Law Firm

Font styles to use
Serif
Sans Serif

Colors
b1b1b1
333333

Requirements
Must have
• Business name: Hartwell Law Firm, Inc.
• Website: www.hartwelllawfirm-example.com
• Telephone: (555)274-1936
• Our firm's logo
Nice to have
• Color preference is black, taupe, and white. A photo for reference of the office coloring is uploaded.
• We currently have an established logo which our firm has been using for more than 10 years. Our logo has been used in advertising, commercials, letterhead, and on-site. We are looking to transition from brown/rust/cream to the black/taupe/white color scheme.
Should not have
• Cheesy slogans; character designs; directions; additional symbols outside of the firm's logo.

```html
<!DOCTYPE html>
<html lang="en">
<head>
<meta charset="utf-8">
<title>Hartwell Law Firm, Inc. – Backlit Sign</title>
<link rel="stylesheet" href="https://fonts.googleapis.com/css2?family=EB+Garamond:wght@500&display=swap">
<style>
  :root {
    --page-bg: #d9d9d9;
    --panel-black: #050505;
    --panel-sheen: #2a2a2a;
    --text-white: #ffffff;
    --mark-copper: #c5732c;
    --mark-copper-light: #e09a55;
  }
  html, body {
    margin: 0;
    padding: 0;
    width: 1200px;
    height: 962px;
    overflow: hidden;
    background: var(--page-bg);
  }
  .canvas {
    position: relative;
    width: 1200px;
    height: 962px;
  }
  .sign-panel {
    position: absolute;
    left: 80px;
    top: 348px;
    width: 1040px;
    height: 266px;
    background: radial-gradient(ellipse 40% 90% at 25% 55%, var(--panel-sheen), var(--panel-black) 70%);
    font-family: "EB Garamond", "Garamond", serif;
    color: var(--text-white);
  }
  .firm-mark {
    position: absolute;
    left: 86px;
    top: 22px;
    width: 180px;
    display: flex;
    flex-direction: column;
    align-items: center;
  }
  .firm-mark__square {
    width: 180px;
    height: 180px;
    background: linear-gradient(135deg, var(--mark-copper-light), var(--mark-copper));
  }
  .firm-mark__name {
    margin-top: 8px;
    font-size: 30px;
    font-weight: 500;
    letter-spacing: 1px;
    line-height: 1;
    color: var(--text-white);
  }
  .sign-details {
    position: absolute;
    left: 370px;
    top: 0;
    right: 20px;
    font-weight: 500;
  }
  .firm-name {
    position: absolute;
    left: 0;
    top: 20px;
    margin: 0;
    font-size: 58px;
    font-weight: 500;
    line-height: 1;
    white-space: nowrap;
  }
  .firm-phone {
    position: absolute;
    left: 54px;
    top: 102px;
    margin: 0;
    font-size: 64px;
    line-height: 1;
    white-space: nowrap;
  }
  .firm-website {
    position: absolute;
    left: 0;
    top: 190px;
    margin: 0;
    font-size: 44px;
    line-height: 1;
    white-space: nowrap;
  }
</style>
</head>
<body>
  <main class="canvas">
    <section class="sign-panel" aria-label="Hartwell Law Firm backlit sign">
      <div class="firm-mark">
        <div class="firm-mark__square"></div>
        <div class="firm-mark__name">HARTWELL</div>
      </div>
      <div class="sign-details">
        <h1 class="firm-name">Hartwell Law Firm, Inc.</h1>
        <p class="firm-phone">(555)274-1936</p>
        <p class="firm-website">www.hartwelllawfirm-example.com</p>
      </div>
    </section>
  </main>
</body>
</html>
```